Restaurant needs take out menu design

I need a takeout menu design for a new restaurant. We will be printing via quillpressly.com. On their website, you can download blank templates.

See specs:
1. 11x17 accordion folding. http://www.quillpressly.com/take-out-menu-printing.html
2. Font is Times New Roman
3. All design/font on the menu will be black

*See menu inspiration attached. Feel free to reuse similar boarders and design.
*Attached is our logo
*Please let me know if any other information is needed.
*Attached is a our menu with prices.
*Please send to me in an ai file.

Industry/Entity Type

Restaurant

Font styles to use
Serif
Decorative

Requirements
Must have
• new times roman. black lettering
• all uppercase lettering
• must be in adobe illustrator format
• have the same feel as the menus I attached
Nice to have
• Leave the area for the telephone numbers, hours, address and business hours the same as the copy and pasted menu.
Should not have
• No other color than black

```html
<!DOCTYPE html>
<html lang="en">
<head>
<meta charset="utf-8">
<title>The Jade Harbor – Takeout Menu</title>
<link href="https://fonts.googleapis.com/css2?family=Tinos:wght@400;700&family=Rye&display=swap" rel="stylesheet">
<style>
  :root{
    --ink:#1a1a1a;
    --paper:#ffffff;
    --panel-dark:#2e2e2e;
    --panel-mid:#464646;
    --rule:#222222;
    --chalk:#f4f4f4;
  }
  *{margin:0;padding:0;box-sizing:border-box}
  html,body{width:930px;height:1200px;overflow:hidden;background:#ffffff}
  .menu{position:relative;width:930px;height:1200px;font-family:"Tinos","Times New Roman",serif;color:var(--ink)}

  /* Cover panel */
  .cover{position:absolute;left:0;top:0;width:458px;height:1200px;
    background:radial-gradient(ellipse at 50% 45%,var(--panel-mid),var(--panel-dark) 75%);color:var(--chalk)}
  .cover-frame{position:absolute;left:14px;top:14px;right:14px;bottom:14px;border:1px solid var(--chalk)}
  .cover-frame-inner{position:absolute;left:22px;top:22px;right:22px;bottom:22px;border:1px solid rgba(244,244,244,.6)}
  .ornament{position:absolute;background:rgba(244,244,244,.18);border-radius:40%}
  .ornament--top{left:179px;top:78px;width:96px;height:48px}
  .ornament--bottom{left:179px;top:1073px;width:96px;height:58px}
  .ornament--side-left{left:86px;top:886px;width:26px;height:118px}
  .ornament--side-right{left:346px;top:886px;width:26px;height:118px}
  .chef-emblem{position:absolute;left:156px;top:666px;width:146px;height:134px;background:rgba(244,244,244,.14);border-radius:50%}
  .brand-name{position:absolute;left:40px;right:40px;top:290px;text-align:center;
    font-weight:400;font-size:36px;letter-spacing:3px;color:var(--chalk)}
  .cover-title{position:absolute;left:0;right:0;top:500px;text-align:center;
    font-family:"Rye","Times New Roman",serif;font-size:74px;color:var(--chalk);letter-spacing:1px}
  .contact{position:absolute;left:0;right:0;top:914px;text-align:center;font-size:25px;line-height:32px;color:var(--chalk)}

  /* Menu panel */
  .listing{position:absolute;left:458px;top:0;width:472px;height:1200px;background:var(--paper)}
  .listing-frame{position:absolute;left:12px;top:14px;right:6px;bottom:14px;border:3px double var(--rule)}
  .section-title{position:absolute;left:0;right:0;text-align:center;font-weight:700;font-size:15px;line-height:18px;letter-spacing:.5px}
  .section-title span{display:inline-block;padding:1px 10px;border-top:1px solid var(--rule);border-bottom:1px solid var(--rule)}
  .section-title--boxed span{border:1px solid var(--rule);padding:2px 10px}
  .item-box{position:absolute;left:38px;width:418px;border:1px solid var(--rule)}
  .item-box--double{border:3px double var(--rule)}
  .items{position:absolute;left:56px;width:380px;list-style:none;font-size:11.6px;line-height:16px}
  .items li{position:relative;height:16px;white-space:nowrap}
  .items .price{position:absolute;right:0;top:0}
  .items .price-alt{position:absolute;right:40px;top:0}
  .items .price-pt{position:absolute;right:46px;top:0}
  .spicy{display:inline-block;width:9px;height:4px;margin:0 2px 2px -12px;background:var(--ink);border-radius:4px;transform:rotate(-35deg)}
</style>
</head>
<body>
<div class="menu">

  <section class="cover">
    <div class="cover-frame"></div>
    <div class="cover-frame-inner"></div>
    <div class="ornament ornament--top" role="img" aria-label="Decorative flourish"></div>
    <h1 class="brand-name">THE JADE HARBOR</h1>
    <div class="cover-title">MENU</div>
    <div class="chef-emblem" role="img" aria-label="Chef hat with crossed fork and knife"></div>
    <div class="ornament ornament--side-left" role="img" aria-label="Decorative scroll"></div>
    <div class="ornament ornament--side-right" role="img" aria-label="Decorative scroll"></div>
    <p class="contact">telephone<br>address<br>business hours</p>
    <div class="ornament ornament--bottom" role="img" aria-label="Decorative flourish"></div>
  </section>

  <section class="listing">
    <div class="listing-frame"></div>

    <h2 class="section-title" style="top:40px"><span>SOUPS</span></h2>
    <div class="item-box" style="top:62px;height:146px"></div>
    <ul class="items" style="top:70px">
      <li><span class="price-pt">PT.</span><span class="price">QT.</span></li>
      <li>EGG DROP SOUP<span class="price-pt">2.75</span><span class="price">4.95</span></li>
      <li><i class="spicy" role="img" aria-label="spicy"></i>HOT &amp; SOUR SOUP<span class="price-pt">3.95</span><span class="price">6.75</span></li>
      <li>WONTON SOUP<span class="price-pt">3.95</span><span class="price">6.75</span></li>
      <li>BEAN CURD SOUP WITH VEGETABLES (2)<span class="price-pt">6.95</span></li>
      <li>CHICKEN CORN SOUP (2)<span class="price-pt">7.95</span></li>
      <li>TEN INGREDIENTS RICE SOUP (2)<span class="price-pt">7.95</span></li>
      <li>SYMPHONY SEAFOOD SOUP (FOR 2)<span class="price-pt">12.95</span></li>
    </ul>

    <h2 class="section-title" style="top:224px"><span>APPETIZERS</span></h2>
    <div class="item-box" style="top:246px;height:450px"></div>
    <ul class="items" style="top:256px">
      <li>VEGETABLE ROLL<span class="price">2.25</span></li>
      <li>EGG ROLL<span class="price">2.50</span></li>
      <li>SHRIMP ROLL<span class="price">2.50</span></li>
      <li>STEAMED EDAMAME<span class="price">3.95</span></li>
      <li>SCALLION PANCAKES<span class="price">4.50</span></li>
      <li><i class="spicy" role="img" aria-label="spicy"></i>COLD NOODLES IN SESAME SAUCE<span class="price">4.95</span></li>
      <li>CRISPY CRAB RAGOON (3)<span class="price">4.95</span></li>
      <li>SHRIMP TOAST (4)<span class="price">5.75</span></li>
      <li>BARBECUED BEEF STICKS (2)<span class="price">5.95</span></li>
      <li>STEAMED DUMPLINGS (6)<span class="price">6.50</span></li>
      <li>PAN FRIED DUMPLINGS (6)<span class="price">6.50</span></li>
      <li><i class="spicy" role="img" aria-label="spicy"></i>DUMPLINGS WITH HOT OIL</li>
      <li>&nbsp;(PEANUT SESAME SAUCE) (6)<span class="price">6.50</span></li>
      <li><i class="spicy" role="img" aria-label="spicy"></i>SPICY CHICKEN DUMPLINGS (10)<span class="price">6.50</span></li>
      <li>STEAMED EDAMAME DUMPLINGS (6)<span class="price">6.50</span></li>
      <li>STEAMED SHRIMP DUMPLINGS (4)<span class="price">6.50</span></li>
      <li>SIU MAI DUMPLINGS (4)<span class="price">6.50</span></li>
      <li>VEGETABLE DUMPLINGS (6)<span class="price">6.50</span></li>
      <li>THREE KINDS OF DUMPLINGS (PORK, VEGETABLE,</li>
      <li>AND SHRIMP)<span class="price">6.95</span></li>
      <li>BONELESS RIBS<span class="price">7.95</span></li>
      <li>BACON SHRIMP ROLLS (6)<span class="price">8.50</span></li>
      <li>BARBECUED SPARE RIBS (4)<span class="price-alt">9.95 (8)</span><span class="price">15.95</span></li>
      <li>PU PU PLATTER (FOR 2)<span class="price">16.95</span></li>
      <li>SHRIMP TOAST, BBQ SPARE RIBS, BEEF STICKS,</li>
      <li>SHRIMP ROLLS, SIU MAI DUMPLINGS, AND FRIED</li>
      <li>DUMPLINGS</li>
    </ul>

    <h2 class="section-title" style="top:714px"><span>CHICKEN</span></h2>
    <div class="item-box" style="top:736px;height:226px"></div>
    <ul class="items" style="top:746px">
      <li>MOO SHU CHICKEN<span class="price">13.50</span></li>
      <li>CHICKEN WITH BROCCOLI<span class="price">13.50</span></li>
      <li>CHICKEN WITH MIXED VEGETABLES<span class="price">13.50</span></li>
      <li>CHICKEN WITH CASHEW NUTS<span class="price">13.50</span></li>
      <li><i class="spicy" role="img" aria-label="spicy"></i>KUNG PO CHICKEN WITH PEANUTS<span class="price">13.50</span></li>
      <li>&nbsp;CHICKEN IN GARLIC SAUCE<span class="price">13.50</span></li>
      <li>CHICKEN WITH STRING BEANS<span class="price">13.50</span></li>
      <li>SWEET &amp; SOUR CHICKEN<span class="price">13.50</span></li>
      <li>CHICKEN WITH EGGPLANT<span class="price">13.95</span></li>
      <li><i class="spicy" role="img" aria-label="spicy"></i>HUNAN CHICKEN WITH BLACK BEAN SAUCE<span class="price">13.95</span></li>
      <li>CHICKEN WITH SNOW PEAS<span class="price">13.95</span></li>
      <li>CHICKEN WITH ASPARAGUS<span class="price">13.95</span></li>
      <li>&nbsp;PEPPERCORN CHICKEN<span class="price">13.95</span></li>
    </ul>

    <h2 class="section-title section-title--boxed" style="top:984px"><span>PORK</span></h2>
    <div class="item-box item-box--double" style="top:1022px;height:104px"></div>
    <ul class="items" style="top:1034px">
      <li>SWEET &amp; SOUR PORK<span class="price">12.95</span></li>
      <li><i class="spicy" role="img" aria-label="spicy"></i>PORK IN GARLIC SAUCE<span class="price">12.95</span></li>
      <li>SLICED PORK WITH MIXED VEGETABLES<span class="price">12.95</span></li>
      <li>SLICED PORK WITH STRING BEANS<span class="price">12.95</span></li>
      <li>MOO SHU PORK<span class="price">12.95</span></li>
    </ul>
  </section>

</div>
</body>
</html>
```